Website Design for Cirrovane Cloud Service

We are building a service to allow customers to own their own private clouds easily and cheaply. Owning your own private cloud saves costs, and offers more flexibility than a public cloud provider but has historically been a complex and expensive option.

We plan to offer a service where we build and maintain your own private cloud on your own hardware for a cheap monthly costs. Similar to this service - https://nimbarvo.com/solutions/private-cloud

We already have a logo and branding in place - we'd like a website design to be tailored from this branding, see attached logo design.

Feel free to add important elements on the home page such as testimonials, client/partner logos, contact form, social media, etc using placeholder contents in addition to the document we attached.

We also plan to add sub-pages in the future so please make sure that your website design has a full navigation menu.

An example of the site we like: https://www.vosketri.com/ we'd be happy for you to take inspiration from this website.

Target Market(s)

B2B focused, we are targeting start-up/small/medium sized companies who needs help with their cloud and IT infrastructure.

Industry/Entity Type

IT

Number of Pages Required

1 page

Font styles to use
Other font styles liked:
• Please refer to the attachment - font must have Mayeka Demi Bold & Retroica

Requirements
Must have
• Please add placeholder menu since we're planning to have subpages later on.

```html
<!DOCTYPE html>
<html lang="en">
<head>
<meta charset="utf-8">
<title>Cirrovane Cloud Service</title>
<link rel="stylesheet" href="https://fonts.googleapis.com/css2?family=Comfortaa:wght@500;700&family=Montserrat:wght@400;500;600;700&display=swap">
<style>
:root{
  --navy:#0a1d4d;
  --navy-deep:#061438;
  --blue:#1e77b3;
  --accent:#1a7cc6;
  --ink:#1b1f2a;
  --muted:#6a7180;
  --soft:#eef1f5;
  --white:#ffffff;
  --star:#f5c518;
}
*{box-sizing:border-box;margin:0;padding:0}
html,body{width:1200px;height:4637px;overflow:hidden}
body{font-family:"Montserrat",sans-serif;color:var(--ink);background:var(--white)}
.page{position:relative;width:1200px;height:4637px;overflow:hidden}
.abs{position:absolute}
.display{font-family:"Comfortaa",sans-serif;font-weight:700}
.btn{position:absolute;display:flex;align-items:center;justify-content:center;border-radius:30px;font-size:11px;font-weight:700;letter-spacing:.5px;text-transform:uppercase;text-decoration:none}
.btn-white{background:var(--white);color:var(--accent)}
.btn-blue{background:var(--accent);color:var(--white)}

/* hero */
.hero-bg{position:absolute;left:0;top:0}
.brand{position:absolute;display:flex;align-items:center;gap:10px;color:var(--white);font-family:"Comfortaa",sans-serif;font-weight:700;font-size:32px}
.brand-dot{width:34px;height:34px;border-radius:50%;background:var(--white)}
.nav{position:absolute;top:70px;left:0;width:1200px;height:20px}
.nav a{position:absolute;color:var(--white);font-size:13px;font-weight:500;text-decoration:none}
.hero-title{top:168px;left:0;width:1200px;text-align:center;color:var(--white);font-size:30px;line-height:35px}
.hero-sub{top:258px;left:0;width:1200px;text-align:center;color:var(--white);font-size:15px;line-height:22px}
.hero-lead{top:351px;left:0;width:1200px;text-align:center;color:var(--white);font-size:15px;font-weight:700}
.hero-art{left:430px;top:378px;width:340px;height:292px;border-radius:170px 170px 40px 40px;background:linear-gradient(180deg,#1f5fb0 0%,#123f86 100%)}

/* features */
.feature{position:absolute;width:230px;text-align:center}
.feature-icon{width:82px;height:82px;margin:0 auto;border-radius:22px;background:var(--white);box-shadow:0 8px 22px rgba(20,50,110,.12);display:flex;align-items:center;justify-content:center}
.feature-icon span{width:38px;height:38px;border-radius:10px;background:linear-gradient(135deg,#cfe4f7,#7fb4e2)}
.feature h3{margin-top:26px;font-size:14px;font-weight:700;line-height:17px}
.feature p{margin-top:12px;font-size:11px;color:var(--muted);line-height:13px}
.benefits-title{left:176px;top:1030px;font-size:38px;line-height:44px;letter-spacing:1px;color:var(--ink)}
.benefits-title em{font-style:normal;color:var(--accent)}
.rule{left:176px;top:1132px;width:396px;height:2px;background:#dfe3ea}
.rule-accent{left:176px;top:1130px;width:76px;height:5px;border-radius:3px;background:var(--accent)}

/* transform band */
.transform-band{left:0;top:1388px;width:1200px;height:517px;background:var(--blue)}
.transform-title{left:158px;top:1468px;color:var(--white);font-size:28px;line-height:33px}
.transform-copy{left:160px;top:1565px;width:445px;color:var(--white);font-size:12px;line-height:22px}
.transform-copy p+p{margin-top:23px}
.transform-art{left:562px;top:1413px;width:638px;height:492px;background:linear-gradient(160deg,#2a7fd0,#13509e 55%,#1a65b0)}
.tag{position:absolute;width:95px;height:88px;background:var(--white);border-radius:6px;box-shadow:0 6px 16px rgba(0,0,0,.15);text-align:center;font-size:13px;font-weight:700;color:var(--ink)}
.tag i{display:block;width:28px;height:28px;margin:14px auto 8px;border-radius:50%;border:2px solid #4f95d6}

/* public cloud */
.public-art{left:36px;top:1989px;width:558px;height:441px;border-radius:8px;background:linear-gradient(150deg,#dcebf9,#b9d6f2)}
.public-title{left:619px;top:1988px;font-size:28px;line-height:33px;color:var(--ink)}
.point{position:absolute;left:619px;width:420px}
.point h4{font-size:12px;font-weight:700}
.point p{margin-top:6px;font-size:11.5px;line-height:22px;color:var(--muted)}

/* testimonial */
.testimonial-band{left:0;top:2565px;width:1200px;height:391px;background:var(--blue);border-bottom-right-radius:220px}
.testimonial-photo{left:153px;top:2601px;width:427px;height:324px;border-radius:150px;background:linear-gradient(135deg,#6b7f96,#2d4d73 60%,#8a7a68)}
.quote-title{left:666px;top:2660px;width:388px;text-align:center;color:var(--white);font-size:26px}
.quote-mark{left:666px;top:2706px;width:388px;text-align:center;color:#cfe3f5;font-family:Georgia,serif;font-size:60px;line-height:50px}
.quote-text{left:666px;top:2756px;width:388px;text-align:center;color:var(--white);font-size:12px;line-height:20px}
.quote-name{left:666px;top:2858px;width:388px;text-align:center;color:var(--white);font-size:14px;font-weight:500}
.stars{left:666px;top:2878px;width:388px;text-align:center;color:var(--star);font-size:16px;letter-spacing:4px}

/* difference */
.diff-title{left:144px;top:3040px;font-size:26px;color:var(--ink)}
.diff-list{position:absolute;left:144px;top:0;width:480px;list-style:none}
.diff-list li{position:absolute;left:0;width:480px;padding-left:31px;font-size:11px;line-height:16px;color:#3a404d}
.diff-list li::before{content:"";position:absolute;left:2px;top:2px;width:15px;height:11px;border-radius:7px 7px 4px 4px;background:#5e6673}
.diff-art{left:640px;top:3030px;width:540px;height:455px;border-radius:8px;background:linear-gradient(150deg,#e3eefa,#b7d3f0)}

/* partners */
.partners-title{left:0;top:3632px;width:1200px;text-align:center;font-size:26px;color:var(--ink)}
.badge{position:absolute;width:144px;height:144px;background:#e3e8ef;display:flex;align-items:center;justify-content:center}
.badge span{width:72px;height:72px;border-radius:50%;background:linear-gradient(160deg,#2a66b8,#1a3f86)}
.badge span.hex{border-radius:14px;transform:rotate(45deg);width:62px;height:62px;background:linear-gradient(160deg,#3b3f9a,#262a72)}

/* footer */
.footer-brand{left:0;top:4134px;width:1200px;justify-content:center}
.contact-head{left:158px;top:4240px;color:var(--white);font-size:11px;font-weight:600;text-decoration:underline}
.contact-row{position:absolute;left:158px;display:flex;gap:18px;color:var(--white);font-size:12px;line-height:22px}
.contact-row svg{flex:none;margin-top:3px}
.social{position:absolute;top:4465px;width:26px;height:26px;border-radius:50%;border:2px solid var(--white)}
.copyright{left:158px;top:4553px;color:var(--white);font-size:10.5px}
.field{position:absolute;background:var(--white);border-radius:24px;font-size:11px;color:#8b919c;padding:14px 22px}
.submit{position:absolute;left:900px;top:4518px;width:135px;height:48px;border-radius:24px;background:var(--white);color:var(--navy);font-size:11px;font-weight:700;display:flex;align-items:center;justify-content:center;text-transform:uppercase}
</style>
</head>
<body>
<div class="page">

  <!-- hero -->
  <svg class="hero-bg" width="1200" height="690" viewBox="0 0 1200 690">
    <defs>
      <linearGradient id="heroFill" x1="0" y1="0" x2="0" y2="1">
        <stop offset="0" stop-color="#071638"/>
        <stop offset="1" stop-color="#0d2d6b"/>
      </linearGradient>
    </defs>
    <path d="M0 0H1200V520Q600 830 0 520Z" fill="url(#heroFill)"/>
  </svg>
  <div class="abs hero-art" role="img" aria-label="Glowing globe with a cloud network illustration"></div>
  <div class="brand" style="left:144px;top:46px"><span class="brand-dot"></span>Cirrovane</div>
  <nav class="nav">
    <a href="#" style="left:562px">Home</a>
    <a href="#" style="left:640px">About</a>
    <a href="#" style="left:716px">Services</a>
    <a href="#" style="left:806px">Why Us</a>
    <a href="#" style="left:894px">Partners</a>
    <a href="#" style="left:986px">Contact</a>
  </nav>
  <h1 class="abs display hero-title">A groundbreaking way for your small business<br>to benefit from the power of the cloud</h1>
  <p class="abs hero-sub">Cirrovane Cloud Service is here to help small businesses utilise the power<br>of the cloud without complicated set-ups or scary price tags.</p>
  <p class="abs hero-lead">Ready to modernise your infrastructure with a fully managed private cloud solution from CVCS?</p>
  <a class="btn btn-white" href="#" style="left:516px;top:400px;width:170px;height:54px;color:var(--navy)">Contact Us</a>

  <!-- benefits -->
  <div class="feature" style="left:160px;top:763px"><div class="feature-icon"><span></span></div><h3>Totally flexible</h3><p>get the cloud you want and the<br>latest innovations you need</p></div>
  <div class="feature" style="left:376px;top:763px"><div class="feature-icon"><span></span></div><h3>Faster</h3><p>our private cloud solutions<br>outpace public clouds</p></div>
  <div class="feature" style="left:587px;top:763px"><div class="feature-icon"><span></span></div><h3>Greater value for money</h3><p>totally transparent pricing for no<br>nasty month-end surprises</p></div>
  <div class="feature" style="left:812px;top:763px"><div class="feature-icon"><span></span></div><h3>No consultancy fees</h3><p>we'll work with you and charge<br>set fees for everything</p></div>
  <h2 class="abs display benefits-title">How <em>CVCS</em> benefits<br>YOUR BUSINESS</h2>
  <div class="abs rule"></div><div class="abs rule-accent"></div>
  <div class="feature" style="left:587px;top:980px"><div class="feature-icon"><span></span></div><h3>Management, monitoring<br>and maintenance</h3><p>they're all included in your<br>monthly price</p></div>
  <div class="feature" style="left:812px;top:980px"><div class="feature-icon"><span></span></div><h3>Tried and tested cloud<br>solutions</h3><p>we'll deploy the right OpenStratum<br>solutions for your business</p></div>

  <!-- transform band -->
  <div class="abs transform-band"></div>
  <div class="abs transform-art" role="img" aria-label="Isometric illustration of a laptop, servers and people on a blue platform"></div>
  <h2 class="abs display transform-title">CVCS can drive your digital<br>transformation today</h2>
  <div class="abs transform-copy">
    <p>Organisations of all shapes and sizes are reaping the time and money saving benefits that the cloud brings.</p>
    <p>But for small businesses seeking to transition, managing the time and financial costs of transitioning, and knowing whether to opt for a public or private cloud can cause you to hit the pause button.</p>
    <p>CVCS is here to help you switch on your cloud transformation in a way that works best for you. We deliver and support fully managed private cloud solutions that are:</p>
  </div>
  <a class="btn btn-white" href="#" style="left:160px;top:1823px;width:158px;height:45px">Get Started</a>
  <div class="tag" style="left:635px;top:1674px"><i></i>Fast</div>
  <div class="tag" style="left:1019px;top:1633px"><i></i>Scalable</div>
  <div class="tag" style="left:736px;top:1845px"><i></i>Easy</div>
  <div class="tag" style="left:1082px;top:1823px"><i></i>Powerful</div>

  <!-- public cloud -->
  <div class="abs public-art" role="img" aria-label="Isometric illustration of a laptop, phone and people working with cloud servers"></div>
  <h2 class="abs display public-title">If you're using a public<br>cloud now</h2>
  <div class="point" style="top:2076px"><h4>You could be paying too much...</h4><p>Public cloud pricing structures have a habit of sneakily scaling up very quickly. With CVCS, you'll always know what you're paying for your private cloud services.</p></div>
  <div class="point" style="top:2189px"><h4>You're likely not getting the benefits of full functionality...</h4><p>Public cloud providers cannot adopt new innovations and functions as quickly and easily as the private cloud solutions you'll get from CVCS.</p></div>
  <div class="point" style="top:2302px"><h4>You'll be tied to the services your provider can provide...</h4><p>Public cloud providers will have a limited suite of products and services to offer you. A CVCS private cloud has no such limitations</p></div>
  <a class="btn btn-blue" href="#" style="left:619px;top:2403px;width:146px;height:43px">Let's Talk</a>

  <!-- testimonial -->
  <div class="abs testimonial-band"></div>
  <div class="abs testimonial-photo" role="img" aria-label="Portrait photo of a smiling customer"></div>
  <h2 class="abs display quote-title">What Our Customer Says</h2>
  <div class="abs quote-mark">&ldquo;</div>
  <p class="abs quote-text">Lorem ipsum dolor sit amet, consectetur adipisicing elit, sed do eiusmod tempor incididunt ut labore et dolore magna aliqua. Ut enim ad minim veniam, quis nostrud exercitation ullamco laboris nisi ut aliquip ex ea commodo consequat.</p>
  <p class="abs quote-name">Marlo Vent</p>
  <div class="abs stars">★★★★★</div>

  <!-- difference -->
  <h2 class="abs display diff-title">The CVCS Difference</h2>
  <ul class="diff-list">
    <li style="top:3094px">We'll quickly get to grips with what your organisation needs, and deliver it via our private cloud solutions.</li>
    <li style="top:3143px">Enjoy the ease of the public cloud, combined with the features, innovations and flexibility of the private cloud.</li>
    <li style="top:3193px">You can focus on your core business while we support you with a dedicated cloud infrastructure.</li>
    <li style="top:3242px">We'll create and deliver the launchpad that will take your business forward.</li>
    <li style="top:3274px">Get the benefits of your own cloud infrastructure and reduce your operational costs</li>
    <li style="top:3323px">Fast and easy computing, storage and network resources</li>
    <li style="top:3355px">Managed operations from private OpenStratum clouds and Helmgrid</li>
    <li style="top:3388px">We'll support your growth and scale your cloud as you need it.</li>
  </ul>
  <a class="btn btn-blue" href="#" style="left:142px;top:3434px;width:146px;height:45px">Let's Talk</a>
  <div class="abs diff-art" role="img" aria-label="Isometric illustration of a laptop uploading to the cloud on a grid"></div>

  <!-- partners -->
  <svg class="abs" style="left:0;top:3560px" width="1200" height="600" viewBox="0 0 1200 600">
    <path d="M0 90Q600 10 1200 90V600H0Z" fill="var(--soft)"/>
  </svg>
  <h2 class="abs display partners-title">Our Parents</h2>
  <div class="badge" style="left:205px;top:3704px"><span class="hex"></span></div>
  <div class="badge" style="left:367px;top:3704px"><span style="border-radius:6px"></span></div>
  <div class="badge" style="left:529px;top:3704px"><span></span></div>
  <div class="badge" style="left:691px;top:3704px"><span style="border-radius:6px"></span></div>
  <div class="badge" style="left:853px;top:3704px"><span class="hex"></span></div>
  <div class="badge" style="left:367px;top:3866px"><span style="background:linear-gradient(160deg,#5aa7e6,#2f7cc4)"></span></div>
  <div class="badge" style="left:529px;top:3866px"><span style="background:none;border:3px dotted #3a86cf"></span></div>
  <div class="badge" style="left:691px;top:3866px"><span class="hex"></span></div>

  <!-- footer -->
  <svg class="abs" style="left:0;top:4050px" width="1200" height="587" viewBox="0 0 1200 587">
    <defs>
      <linearGradient id="footFill" x1="0" y1="0" x2="0" y2="1">
        <stop offset="0" stop-color="#0a1d4d"/>
        <stop offset="1" stop-color="#0d2d6b"/>
      </linearGradient>
    </defs>
    <path d="M0 75Q600 -30 1200 75V587H0Z" fill="url(#footFill)"/>
  </svg>
  <div class="brand footer-brand"><span class="brand-dot"></span>Cirrovane</div>
  <p class="abs contact-head">CONTACT US</p>
  <div class="contact-row" style="top:4284px">
    <svg width="14" height="18" viewBox="0 0 14 18"><path d="M7 0C3 0 0 3 0 7c0 5 7 11 7 11s7-6 7-11c0-4-3-7-7-7zm0 10a3 3 0 110-6 3 3 0 010 6z" fill="#fff"/></svg>
    <span>Add your address line<br>here abc 123456</span>
  </div>
  <div class="contact-row" style="top:4350px">
    <svg width="16" height="16" viewBox="0 0 16 16"><path d="M3 0l3 4-2 2c1 2 4 5 6 6l2-2 4 3-2 3C7 16 0 9 0 3z" fill="#fff"/></svg>
    <span>+01 23 456 7890</span>
  </div>
  <div class="contact-row" style="top:4395px">
    <svg width="16" height="12" viewBox="0 0 16 12"><rect width="16" height="12" rx="1" fill="#fff"/><path d="M1 1l7 6 7-6" stroke="#0a1d4d" stroke-width="1.5" fill="none"/></svg>
    <span>info@cirrovaneservice.com</span>
  </div>
  <span class="social" style="left:162px" aria-label="Social link"></span>
  <span class="social" style="left:221px" aria-label="Social link"></span>
  <span class="social" style="left:282px" aria-label="Social link"></span>
  <span class="social" style="left:343px" aria-label="Social link"></span>
  <p class="abs copyright">© 2022 Cirrovane Cloud Service. All Rights Reserved</p>

  <div class="field" style="left:535px;top:4230px;width:500px;height:47px">Name</div>
  <div class="field" style="left:535px;top:4302px;width:233px;height:47px">Email</div>
  <div class="field" style="left:797px;top:4302px;width:238px;height:47px">Number</div>
  <div class="field" style="left:535px;top:4370px;width:500px;height:126px">Description</div>
  <div class="submit">Submit</div>

</div>
</body>
</html>
```